Website redesign

Redesign the Website

http://www.lindmark-schoefer.de/

Task

- make 1 Layout for the Website
- Colors: white, yellow, brown
- Text: Take from Page - ore rather Use Latin - Lore Ipsum ...
- pimp design and overall look
- enhance overview for better orientation
- more freindly / sympatic overall look.
- Better integrate Mingleroo Button aso.
- send Layout as layered PSD

```html
<!DOCTYPE html>
<html lang="de">
<head>
<meta charset="utf-8">
<title>Lindmark-Schoefer – Trauringe</title>
<link rel="stylesheet" href="https://fonts.googleapis.com/css2?family=Open+Sans:wght@400;600;700;800&display=swap">
<style>
:root{
  --yellow:#e9b90e;
  --yellow-soft:#f2cf3c;
  --brown:#5b2b12;
  --brown-dark:#3f1c0a;
  --cream:#f4efe3;
  --text:#4a4a4a;
  --muted:#9a9a9a;
  --line:#e6e6e6;
  --footer:#efefef;
}
*{margin:0;padding:0;box-sizing:border-box}
html,body{width:1200px;height:2284px;overflow:hidden;background:#fff}
body{font-family:"Open Sans",Arial,sans-serif;color:var(--text);position:relative}
.topbar{height:44px;background:var(--yellow);color:#fff;font-size:15px;display:flex;align-items:center;gap:36px;padding-left:100px}
.topbar span{display:flex;align-items:center;gap:8px}
.header{height:136px;display:flex;align-items:center;justify-content:space-between;padding:0 96px;border-bottom:1px solid var(--line)}
.brand{display:flex;align-items:center;gap:12px;font-size:30px;font-weight:700;color:var(--brown);letter-spacing:.5px}
.brand i{width:16px;height:16px;border-radius:50%;background:var(--yellow);display:block}
.nav{display:flex;gap:6px;font-size:15px;font-weight:600}
.nav a{color:#555;text-decoration:none;padding:12px 14px}
.nav a.active{background:var(--brown);color:#fff}
.hero{position:relative;height:460px;background:linear-gradient(90deg,#efe6d3 0%,#f6f1e6 55%,#efe7d6 100%)}
.hero .visual{position:absolute;left:160px;top:40px;width:470px;height:380px;border-radius:40px;background:radial-gradient(ellipse at 50% 50%,#e4c36a 0%,#d9c9a8 45%,rgba(239,230,211,0) 72%)}
.hero .copy{position:absolute;right:100px;top:150px;text-align:right}
.hero .copy p{font-size:26px;color:#6a5a4a;line-height:1.45}
.hero .copy strong{display:block;font-size:30px;color:var(--yellow);font-weight:700;margin-top:10px}
.dots{position:absolute;left:0;right:0;top:400px;display:flex;justify-content:center;gap:10px}
.dots i{width:11px;height:11px;border-radius:50%;background:#555;display:block}
.dots i:first-child{background:var(--yellow)}
.editions{position:absolute;top:672px;left:96px;right:96px;display:flex;justify-content:space-between}
.edition{width:320px;height:216px;position:relative}
.edition .photo{position:absolute;inset:0;background:linear-gradient(135deg,#d8b9a0,#f1e3d6 60%,#c9ad97)}
.edition:nth-child(3) .photo{background:linear-gradient(135deg,#bfb6ad,#e9e4de 55%,#a79d93)}
.edition .ribbon{position:absolute;left:50%;top:150px;transform:translateX(-50%);width:220px;height:44px;background:var(--brown);color:#fff;font-size:19px;font-weight:600;display:flex;align-items:center;justify-content:center;letter-spacing:1px;clip-path:polygon(16px 0,calc(100% - 16px) 0,100% 50%,calc(100% - 16px) 100%,16px 100%,0 50%)}
.edition:nth-child(2) .ribbon{background:var(--yellow)}
.section-title{position:absolute;left:0;right:0;text-align:center;font-size:26px;font-weight:700;color:var(--brown)}
.bestseller-title{top:934px}
.products{position:absolute;top:988px;left:96px;right:96px;display:flex;justify-content:space-between}
.product{width:188px;height:212px;border:1px solid var(--line);text-align:center;padding-top:18px;background:#fff}
.product .ring{width:120px;height:100px;margin:0 auto 10px;border-radius:50%;background:radial-gradient(circle,#f7e08a 0%,#d9ad2a 45%,rgba(255,255,255,0) 70%)}
.product.silver .ring{background:radial-gradient(circle,#f1f1f1 0%,#b9b9b9 45%,rgba(255,255,255,0) 70%)}
.product.bicolor .ring{background:radial-gradient(circle,#eee 0%,#d8b440 45%,rgba(255,255,255,0) 70%)}
.product p{font-size:13px;line-height:1.35;color:#555}
.product p b{font-weight:700;color:#333}
.collection{position:absolute;top:1256px;left:0;right:0;height:424px;background:linear-gradient(180deg,var(--yellow-soft),var(--yellow));text-align:center;padding-top:118px}
.collection h2{color:#fff;font-size:48px;font-weight:800;letter-spacing:1px}
.collection h3{color:var(--brown);font-size:28px;font-weight:700;margin-top:18px}
.collection h3::after{content:"";display:block;width:120px;height:2px;background:var(--brown);margin:14px auto 0;opacity:.5}
.btn{display:inline-block;margin-top:24px;background:var(--brown);color:#fff;font-size:16px;padding:12px 30px}
.bottom-title{position:absolute;top:1716px;font-size:26px;font-weight:600;color:#555}
.clients{position:absolute;top:1790px;left:96px;width:440px;display:grid;grid-template-columns:repeat(3,1fr);row-gap:44px;column-gap:20px}
.client{display:flex;align-items:center;gap:8px;color:#9d9d9d;font-size:15px;font-weight:700;height:36px}
.client i{width:22px;height:22px;background:#c7c7c7;display:block;flex:none}
.client i.round{border-radius:50%}
.video{position:absolute;top:1780px;left:608px;width:496px;height:280px;background:linear-gradient(135deg,#c8b8a6,#efe6da 50%,#b8a38c)}
.video .play{position:absolute;left:50%;top:50%;width:72px;height:50px;margin:-25px 0 0 -36px;border-radius:12px;background:rgba(40,40,40,.85);display:flex;align-items:center;justify-content:center}
.video .bar{position:absolute;left:0;right:0;bottom:0;height:30px;background:rgba(20,20,20,.75)}
.footer{position:absolute;top:2120px;left:0;right:0;height:164px;background:var(--footer);text-align:center;padding-top:36px}
.social{display:flex;justify-content:center;gap:12px}
.social i{width:28px;height:28px;border-radius:50%;background:var(--yellow);display:block}
.footer-nav{margin-top:18px;font-size:14px;color:#666;display:flex;justify-content:center;gap:14px}
.footer-nav em{font-style:normal;color:#bbb}
.powered{margin-top:14px;font-size:14px;font-weight:700;color:#555}
</style>
</head>
<body>
<div class="topbar">
  <span><svg width="14" height="14" viewBox="0 0 24 24" fill="#fff"><path d="M6.6 10.8a15 15 0 0 0 6.6 6.6l2.2-2.2c.3-.3.7-.4 1-.2 1.1.4 2.3.6 3.6.6.6 0 1 .4 1 1V20c0 .6-.4 1-1 1A17 17 0 0 1 3 4c0-.6.4-1 1-1h3.5c.6 0 1 .4 1 1 0 1.3.2 2.5.6 3.6.1.3 0 .7-.2 1z"/></svg>0123 456789</span>
  <span><svg width="16" height="12" viewBox="0 0 24 18" fill="#fff"><path d="M0 0h24v18H0z" fill="none"/><path d="M2 0h20a2 2 0 0 1 2 2v.5L12 10 0 2.5V2a2 2 0 0 1 2-2zm-2 5 12 7.5L24 5v11a2 2 0 0 1-2 2H2a2 2 0 0 1-2-2z"/></svg>info@lindmark-schoefer.de</span>
</div>
<header class="header">
  <div class="brand"><i></i>Lindmark-Schoefer.de</div>
  <nav class="nav">
    <a class="active">Zehnen</a><a>Trauringe</a><a>Solitärringe</a><a>Partnerringe</a><a>Brautschmuck</a><a>Informationen</a><a>Kontakt</a>
  </nav>
</header>
<section class="hero">
  <div class="visual" role="img" aria-label="Zwei Trauringe aus Gold und Weißgold mit Brillant"></div>
  <div class="copy">
    <p>Ihr Weg zum Glück...<br>...jetzt unter neuer Adresse!</p>
    <strong>In der Rosengasse 12, 10115 Musterstadt</strong>
  </div>
  <div class="dots"><i></i><i></i><i></i><i></i></div>
</section>
<section class="editions">
  <div class="edition"><div class="photo" role="img" aria-label="Hände eines Paares mit Trauringen"></div><div class="ribbon">EDITION 1</div></div>
  <div class="edition"><div class="photo" role="img" aria-label="Verschränkte Hände mit Eheringen"></div><div class="ribbon">EDITION 2</div></div>
  <div class="edition"><div class="photo" role="img" aria-label="Exklusiver Ring mit Brillant"></div><div class="ribbon">EXKLUSIV</div></div>
</section>
<h2 class="section-title bestseller-title">BEST SELLER</h2>
<section class="products">
  <div class="product"><div class="ring" role="img" aria-label="Trauringpaar Gelbgold"></div><p><b>5324</b><br>Gelbgold<br>1 Brillant 0,05 Carat</p></div>
  <div class="product"><div class="ring" role="img" aria-label="Trauringpaar Gelbgold"></div><p><b>5324</b><br>Gelbgold<br>1 Brillant 0,05 Carat</p></div>
  <div class="product bicolor"><div class="ring" role="img" aria-label="Trauringpaar Bicolor"></div><p><b>5324</b><br>Gelbgold<br>1 Brillant 0,05 Carat</p></div>
  <div class="product"><div class="ring" role="img" aria-label="Trauringpaar Gelbgold"></div><p><b>5324</b><br>Gelbgold<br>1 Brillant 0,05 Carat</p></div>
  <div class="product silver"><div class="ring" role="img" aria-label="Trauringpaar Weißgold"></div><p><b>5324</b><br>Gelbgold<br>1 Brillant 0,05 Carat</p></div>
</section>
<section class="collection">
  <h2>NEUE KOLLEKTION</h2>
  <h3>Neueste Trends im Jahr 2015</h3>
  <span class="btn">View More</span>
</section>
<h2 class="bottom-title" style="left:96px">Unsere Klienten</h2>
<h2 class="bottom-title" style="left:608px">Unsere Video</h2>
<div class="clients">
  <div class="client"><i></i>Your Company</div>
  <div class="client"><i class="round"></i>Company</div>
  <div class="client"><i class="round"></i>LOGO</div>
  <div class="client"><i></i>Business</div>
  <div class="client"><i class="round"></i>Your Business</div>
  <div class="client"><i></i>Your Logo</div>
  <div class="client"><i></i>Your Logo</div>
  <div class="client"><i class="round"></i>Business</div>
  <div class="client"><i></i>Your Logo</div>
</div>
<div class="video" role="img" aria-label="Videovorschau: Trauringe in der Werkstatt">
  <div class="play"><svg width="22" height="24" viewBox="0 0 22 24"><path d="M0 0l22 12L0 24z" fill="#fff"/></svg></div>
  <div class="bar"></div>
</div>
<footer class="footer">
  <div class="social"><i></i><i></i><i></i><i></i></div>
  <div class="footer-nav"><span>Zehnen</span><em>//</em><span>Trauringe</span><em>//</em><span>Solitärringe</span><em>//</em><span>Partnerringe</span><em>//</em><span>Brautschmuck</span><em>//</em><span>Informationen</span><em>//</em><span>Kontakt</span></div>
  <div class="powered">Powered By lindmark-schoefer.de © 2015</div>
</footer>
</body>
</html>
```